Manuka honey wholesales and exports

We need business cards for our honey distribution company based in New Zealand. We supply shops locally and export Manuka honey around the world.
We deal with a very high quality and 100% natural product that can be used for medical, general health as well as food. We are looking business cards that show our honey products are of a high quality with a modern look.

Target Market(s)

Health and medical retailers and importers

Industry/Entity Type

Wholesale

Contact Information for Business Card

Tevin Apiary NZ Limited

www.tevinapiarynz.example

Derek Fawley

M +64 219036482

E tevinapiarynz@mailbox.example

PO Box 58-214
Takapuna
North Shore
Auckland
New Zealand

Font styles to use
Serif

Requirements
Must have
• (Tevin Apiary NZ Limited) with some artwork on one side and all details on the other side.
Nice to have
• I have seen a very simple card with large yellow and black stripes on one side with a company name.. looked clean and simple so something similar or just let the creative beast inside you take over and we will see what you can come up with.

```html
<!DOCTYPE html>
<html lang="en">
<head>
<meta charset="utf-8">
<title>Tevin Apiary NZ Limited — Business Card</title>
<link rel="stylesheet" href="https://fonts.googleapis.com/css2?family=Open+Sans:wght@300;400;700&display=swap">
<style>
  :root {
    --page-bg: #dcdcdc;
    --card-bg: #232323;
    --accent: #e01b1f;
    --ink-light: #f2f2f2;
    --ink-muted: #cfcfcf;
  }
  html, body {
    margin: 0;
    width: 1200px;
    height: 1200px;
    overflow: hidden;
    background: var(--page-bg);
    font-family: "Open Sans", Arial, sans-serif;
  }
  .sheet {
    position: relative;
    width: 1200px;
    height: 1200px;
  }
  .card {
    position: absolute;
    left: 120px;
    width: 960px;
    height: 548px;
    background: var(--card-bg);
    box-shadow: 0 6px 18px rgba(0,0,0,0.25);
  }
  .card--front { top: 40px; }
  .card--back { top: 612px; }
  .card svg { display: block; width: 960px; height: 548px; }
  .rule { stroke: var(--accent); stroke-width: 1.2; }
  .band { fill: var(--accent); }
  .company-accent { fill: var(--accent); font-weight: 700; font-size: 44px; }
  .company-rest { fill: var(--ink-light); font-weight: 700; font-size: 44px; }
  .company-url { fill: var(--accent); font-size: 26px; }
  .person-name { fill: var(--ink-light); font-weight: 300; font-size: 40px; }
  .person-role { fill: var(--accent); font-size: 26px; }
  .contact-badge { fill: var(--accent); }
  .contact-badge-letter { fill: #fff; font-weight: 700; font-size: 15px; }
  .contact-text { fill: var(--ink-muted); font-size: 21px; }
</style>
</head>
<body>
<main class="sheet">

  <section class="card card--front" aria-label="Card front">
    <svg viewBox="0 0 960 548" xmlns="http://www.w3.org/2000/svg">
      <g class="rules rules--top">
        <line class="rule" x1="0" y1="34" x2="960" y2="34"/>
        <line class="rule" x1="0" y1="42" x2="960" y2="42"/>
        <line class="rule" x1="0" y1="50" x2="960" y2="50"/>
        <line class="rule" x1="0" y1="62" x2="960" y2="62"/>
      </g>
      <g class="rules rules--bottom">
        <line class="rule" x1="0" y1="486" x2="960" y2="486"/>
        <line class="rule" x1="0" y1="498" x2="960" y2="498"/>
        <line class="rule" x1="0" y1="506" x2="960" y2="506"/>
        <line class="rule" x1="0" y1="514" x2="960" y2="514"/>
      </g>
      <text x="56" y="206">
        <tspan class="company-accent">TEVIN APIARY </tspan><tspan class="company-rest">NZ LIMITED</tspan>
      </text>
      <path class="band" d="M0 222 H560 L580 240 L560 258 H0 Z"/>
      <text class="company-url" x="66" y="300">www.tevinapiarynz.example</text>
    </svg>
  </section>

  <section class="card card--back" aria-label="Card back">
    <svg viewBox="0 0 960 548" xmlns="http://www.w3.org/2000/svg">
      <g class="rules rules--top">
        <line class="rule" x1="0" y1="28" x2="960" y2="28"/>
        <line class="rule" x1="0" y1="36" x2="960" y2="36"/>
        <line class="rule" x1="0" y1="44" x2="960" y2="44"/>
      </g>
      <g class="rules rules--bottom">
        <line class="rule" x1="0" y1="500" x2="960" y2="500"/>
        <line class="rule" x1="0" y1="508" x2="960" y2="508"/>
        <line class="rule" x1="0" y1="516" x2="960" y2="516"/>
      </g>
      <text class="person-name" x="96" y="112">Derek Fawley</text>
      <text class="person-role" x="100" y="150">Director</text>
      <rect class="band" x="0" y="168" width="380" height="34"/>

      <g class="contact-list">
        <g class="contact-row">
          <circle class="contact-badge" cx="430" cy="272" r="14"/>
          <text class="contact-badge-letter" x="430" y="277" text-anchor="middle">P</text>
          <text class="contact-text" x="456" y="280">+64 219036482</text>
          <line class="rule" x1="456" y1="292" x2="960" y2="292"/>
        </g>
        <g class="contact-row">
          <circle class="contact-badge" cx="430" cy="318" r="14"/>
          <text class="contact-badge-letter" x="430" y="323" text-anchor="middle">M</text>
          <text class="contact-text" x="456" y="326">tevinapiarynz@mailbox.example</text>
          <line class="rule" x1="456" y1="338" x2="960" y2="338"/>
        </g>
        <g class="contact-row">
          <circle class="contact-badge" cx="430" cy="364" r="14"/>
          <text class="contact-badge-letter" x="430" y="369" text-anchor="middle">W</text>
          <text class="contact-text" x="456" y="372">www.tevinapiarynz.example</text>
          <line class="rule" x1="456" y1="384" x2="960" y2="384"/>
        </g>
        <g class="contact-row">
          <circle class="contact-badge" cx="430" cy="410" r="14"/>
          <text class="contact-badge-letter" x="430" y="415" text-anchor="middle">A</text>
          <text class="contact-text" x="456" y="418">PO Box 58-214, Takapuna North</text>
          <line class="rule" x1="416" y1="432" x2="960" y2="432"/>
          <text class="contact-text" x="416" y="460">Shore, Auckland, New Zealand</text>
        </g>
      </g>
    </svg>
  </section>

</main>
</body>
</html>
```